Game, Voice & Dedicated Server Company Needs a Business Card Design

We need a new business card design, centered around our new logo (PSD provided below).

Designs that we do like:
https://plomvaste.net/item/corporate-business-card/5382047?s_rank=31 (needs to be made more eye catching)

Our main areas of business are:
- Dedicated Servers
- Game Servers
- Voice Servers
- Mitigation Security Specialists

Industry/Entity Type

Business

Contact Information for Business Card

On the card: (and anything else you would suggest)
- Staff member name
- Staff member position in company
- Staff member phone number
- Staff member email
- Other / Staff member Skype
- Website link

Colors
9bcb3c
abd036

Requirements
Must have
• Design of Card:
• - Green (same green as the logo)
• - Business / Corporate design
• - Something a little different / abstract that shouts premium

```html
<!DOCTYPE html>
<html lang="en">
<head>
<meta charset="utf-8">
<title>Brightpath Hosting – Business Card</title>
<link rel="stylesheet" href="https://fonts.googleapis.com/css2?family=Montserrat:wght@400;600;800&display=swap">
<style>
  :root {
    --stage: #e9e6e1;
    --card: #151515;
    --card-edge: #0b0b0b;
    --green: #9bcb3c;
    --green-light: #abd036;
    --grey: #b9b9b9;
    --grey-dim: #9a9a9a;
    --ink: #111111;
  }
  * { box-sizing: border-box; margin: 0; padding: 0; }
  html, body {
    width: 1200px;
    height: 780px;
    overflow: hidden;
    background: var(--stage);
    font-family: "Montserrat", Arial, sans-serif;
  }
  .stage {
    position: relative;
    width: 1200px;
    height: 780px;
    display: flex;
    justify-content: center;
    align-items: center;
    gap: 80px;
  }
  .card {
    position: relative;
    width: 360px;
    height: 630px;
    background: var(--card);
    border-radius: 4px;
    box-shadow: 0 10px 30px rgba(0, 0, 0, 0.25);
    overflow: hidden;
    display: flex;
    flex-direction: column;
    align-items: center;
  }
  .brand {
    display: flex;
    align-items: center;
    gap: 14px;
    margin-top: 120px;
  }
  .brand-mark {
    width: 22px;
    height: 22px;
    background: var(--green);
  }
  .brand-name {
    color: var(--green);
    font-weight: 800;
    font-size: 28px;
    letter-spacing: 0.5px;
    line-height: 1.05;
    text-transform: uppercase;
  }
  .contact {
    margin-top: 70px;
    text-align: center;
  }
  .contact-name {
    color: var(--green);
    font-weight: 800;
    font-size: 22px;
    letter-spacing: 1px;
    text-transform: uppercase;
  }
  .contact-role {
    color: var(--grey);
    font-size: 16px;
    margin-bottom: 20px;
  }
  .contact-line {
    color: var(--grey);
    font-size: 16px;
    line-height: 1.55;
  }
  .services {
    margin-top: 90px;
    list-style: none;
    text-align: center;
  }
  .services li {
    color: var(--grey);
    font-size: 17px;
    line-height: 1.55;
  }
  .card-band {
    position: absolute;
    left: 0;
    right: 0;
    bottom: 0;
    height: 78px;
    background: var(--green);
    display: flex;
    align-items: center;
    justify-content: center;
  }
  .card-band .web {
    color: var(--ink);
    font-size: 17px;
    letter-spacing: 0.5px;
  }
</style>
</head>
<body>
  <main class="stage">
    <article class="card card-front">
      <div class="brand">
        <span class="brand-mark"></span>
        <span class="brand-name">Brightpath<br>Hosting</span>
      </div>
      <div class="contact">
        <p class="contact-name">John Smith</p>
        <p class="contact-role">Manager</p>
        <p class="contact-line">123 456 7890</p>
        <p class="contact-line">your@yourcompany.com</p>
        <p class="contact-line">yourskypeid</p>
      </div>
      <div class="card-band"><span class="web">www.yourcompany.com</span></div>
    </article>

    <article class="card card-back">
      <div class="brand">
        <span class="brand-mark"></span>
        <span class="brand-name">Brightpath<br>Hosting</span>
      </div>
      <ul class="services">
        <li>Dedicated Servers</li>
        <li>Game Servers</li>
        <li>Voice Servers</li>
        <li>Business relations</li>
      </ul>
      <div class="card-band"><span class="web">www.yourcompany.com</span></div>
    </article>
  </main>
</body>
</html>
```